[Fun Project] Design A Website For A Semi Pro Soccer Team!

DESIGN ONLY! [NO CODING NEEDED]

Hey,

Thanks for looking! Are you ready to design a cool project with us?

This may be a once in a lifetime opportunity to design a website for a Semi Pro Soccer Team. Projects like this don't come along very often! This will be a lot of fun for you!

We need a fresh and exciting website design for a new soccer (or football, depending on where you are) team. You can view the existing site here: http://www.trevmorafc.com/

You can get a sense of the team colors and whatnot from that, but the layout is a little dull. We need something more like this: http://www.bellvanequails.com.

We need something that is visual and exciting, something that will appeal to a sports fan. Ideally, we'd love to work with a designer is a fan of the game, as we think he/she would design something more appealing to the demographic.

Be sure to follow the link below and check out our video:

http://clipdrovo.com/user4417302/review/55820147/3c1f0a7d9e

Thank you and good luck!

Target Market(s)

Soccer/football fans and those interested in becoming fans. More than likely, we're talking males 18-40, but don't want to rule out females.

Industry/Entity Type

Work

Font styles to use
Sans Serif

Colors
faee3e
fbed22
eb1f27
000000
f6f6f6

Requirements
Must have
• Picture/video slider in the top left (see video)
1 home page design and 2 interior page designs
Should not have
• Cluttered
Dull
Lame
Poor Design
And for the love of all the is holy please do not submit us a theme or a template from some website. We are smarter then that and will just remove you from the project....REAL Designers, we got your back and won't even consider crappy stuff....

```html
<!DOCTYPE html>
<html lang="en">
<head>
<meta charset="utf-8">
<title>Trevmora FC — Home</title>
<link rel="stylesheet" href="https://fonts.googleapis.com/css2?family=Montserrat:wght@400;600;700&family=Signika:wght@400;600&family=PT+Sans:wght@400;700&display=swap">
<style>
:root{
  --red:#eb1f27;
  --red-deep:#c41d22;
  --yellow:#fbed22;
  --gold:#f2c230;
  --black:#000;
  --panel:#f6f6f6;
  --grey-text:#8a8a8a;
  --title-text:#444;
  --sky:#5bbde9;
  --fb:#3b6fd8;
}
*{box-sizing:border-box;margin:0;padding:0}
html,body{width:1200px;height:1126px;overflow:hidden}
body{position:relative;font-family:"PT Sans",sans-serif;background:linear-gradient(180deg,#252c3c 0,#3a3f52 280px,#8b2a34 420px,#d42328 560px,#d02226 1025px,#1e1e1e 1025px)}
.side-photo{position:absolute;top:30px;height:995px}
.side-photo.left{left:0;width:233px;background:linear-gradient(180deg,rgba(40,48,66,0) 0,rgba(120,40,40,.5) 380px,rgba(200,40,40,.4) 620px,rgba(210,35,40,0) 900px)}
.side-photo.right{right:0;width:227px;background:linear-gradient(180deg,rgba(60,90,150,.35) 0,rgba(50,100,180,.45) 280px,rgba(150,60,70,.3) 520px,rgba(210,35,40,0) 800px)}
/* top bar */
.topbar{position:absolute;top:0;left:233px;width:740px;height:28px;background:#0c0c0c;display:flex;align-items:center;padding:0 8px 0 9px;gap:6px}
.auth{border:1px solid #777;border-radius:3px;color:#fff;font:700 9px "Montserrat",sans-serif;padding:3px 4px;white-space:nowrap}
.network{color:#fff;font:700 8px/1 "Montserrat",sans-serif;width:44px;text-align:center}
.crests{display:flex;gap:6px;align-items:center}
.crest{width:14px;height:14px;border-radius:50%;background:#4a5a88;border:1px solid #9aa}
.crests span{color:#fff;font:700 8px "Montserrat",sans-serif}
.search{margin-left:auto;width:105px;height:16px;background:#fff;font-size:9px;color:#666;padding:2px 4px}
.feed{width:16px;height:16px;background:#f08a1a;border-radius:2px}
/* header */
.header{position:absolute;top:28px;left:233px;width:740px;height:73px;background:rgba(18,20,28,.82)}
.crest-logo{position:absolute;left:28px;top:10px;width:82px;height:82px;border-radius:50%;background:var(--red);border:3px solid #fff;display:flex;align-items:center;justify-content:center;text-align:center;color:#fff;font:700 12px/1.1 "Montserrat",sans-serif;z-index:3}
.nav{position:absolute;left:149px;top:41px;display:flex;font:600 12px "Montserrat",sans-serif;letter-spacing:.4px}
.nav a{color:#fff;text-decoration:none;padding:0 8px;border-left:1px solid #666}
.nav a:first-child{border:0;padding-left:0;color:var(--yellow)}
/* main */
.main{position:absolute;top:101px;left:233px;width:740px;height:924px;background:#fff}
.abs{position:absolute}
.hero{left:15px;top:25px;width:465px;height:214px;background:linear-gradient(120deg,#3a1416 0,#9a2a2c 45%,#c23a36 70%,#7a2022 100%)}
.hero-title{position:absolute;right:14px;top:106px;text-align:right;color:#fff;font:600 36px/1.05 "Signika",sans-serif}
.hero-sub{position:absolute;right:14px;top:184px;color:var(--gold);font:600 18px "Signika",sans-serif;letter-spacing:1.5px}
.ticker{left:15px;top:239px;width:465px;height:48px;background:linear-gradient(#2a2a2a,#0e0e0e);display:flex}
.ticker div{flex:1;min-width:0;border-left:1px solid #444;padding:11px 10px 0;color:#fff;font:600 11px "Montserrat",sans-serif}
.ticker div:first-child{border:0;color:var(--yellow)}
.ticker small{display:block;color:#999;font:400 8.5px "PT Sans",sans-serif;margin-top:4px;white-space:nowrap;overflow:hidden}
.tab{background:var(--red);color:#fff;font:600 10px "Montserrat",sans-serif;padding:6px 10px;height:20px}
.standings{left:496px;top:26px;width:232px}
.standings .tab{width:120px}
.standings table{width:100%;background:#e8e6e6;border-collapse:collapse;font:400 10px "Montserrat",sans-serif;color:#555}
.standings th{background:#e0d9d9;font-weight:600;color:#333;height:25px;text-align:left;padding-left:8px}
.standings td{height:20px;padding-left:8px;vertical-align:middle}
.standings tr:last-child td{height:26px;vertical-align:top;padding-top:3px}
.video{left:494px;top:151px;width:234px;height:138px;background:linear-gradient(135deg,#3b4048,#6a7280 55%,#2b3a62)}
.video-bar{position:absolute;left:0;bottom:0;width:100%;height:8px;background:#111}
.video-bar::before{content:"";position:absolute;left:6px;top:3px;width:50px;height:2px;background:var(--red)}
.card{top:318px;width:226px;height:113px}
.card .tab{position:absolute;top:0;left:0;width:128px}
.card-body{position:absolute;top:22px;left:0;width:100%;height:91px;background:linear-gradient(90deg,#5d5f63,#9a9ea0);padding:19px 14px;color:#fff;font:600 13.5px/1.25 "Montserrat",sans-serif}
.card-art{position:absolute;right:0;top:-12px;width:110px;height:103px;background:linear-gradient(160deg,rgba(230,40,40,.55),rgba(255,255,255,.15))}
.radio-badge{position:absolute;right:12px;top:13px;width:98px;height:70px;background:#fff;border:2px solid var(--red);display:flex;flex-direction:column;align-items:center;justify-content:center;color:var(--red);font:700 12px/1.3 "Montserrat",sans-serif;text-align:center}
.radio-badge small{color:#000;font-size:8px}
.news-tab{left:15px;top:457px;width:120px}
.news{left:15px;width:495px;height:106px}
.news-img{position:absolute;left:0;top:0;width:106px;height:106px}
.news h3{position:absolute;left:121px;top:4px;width:345px;color:var(--title-text);font:600 19px/1.3 "Signika",sans-serif}
.news p{position:absolute;left:121px;width:355px;color:var(--grey-text);font:400 10px/1.3 "PT Sans",sans-serif}
.feed-box{left:497px;top:451px;width:220px;height:196px;border:1px solid #ddd;background:var(--panel)}
.feed-head{height:43px;background:var(--sky);color:#fff;font:600 13px "Signika",sans-serif;padding:13px 16px;display:flex;gap:8px;align-items:center}
.feed-dot{width:14px;height:14px;border-radius:50%;background:#fff}
.feed-user{position:absolute;top:60px;left:14px;display:flex;gap:10px}
.feed-avatar{width:40px;height:40px;border-radius:50%;background:var(--red)}
.feed-user b{font:400 12px "PT Sans",sans-serif;color:#555;display:block}
.feed-user small{font-size:8px;color:#bbb}
.feed-text{position:absolute;top:126px;left:15px;right:16px;color:#aaa;font:400 9.5px/1.7 "PT Sans",sans-serif}
.feed-text em{font-style:normal;color:#2a8fd0}
.follow{top:659px;width:106px;height:34px;color:#fff;font:600 9px "Montserrat",sans-serif;display:flex;align-items:center;justify-content:center}
.ad{left:497px;top:712px;width:226px;height:187px;background:radial-gradient(circle at 60% 70%,#7a3a80,#2a2440 60%,#15121f)}
.ad-text{position:absolute;left:11px;top:33px;color:#ff3b6b;font:600 22px/1 "Signika",sans-serif}
.ad-cta{position:absolute;right:12px;bottom:11px;color:#fff;font:700 7px "Montserrat",sans-serif}
/* footer */
.footer{position:absolute;top:1025px;left:0;width:1200px;height:101px;background:#1e1e1e}
.foot-logo{position:absolute;left:247px;top:18px;width:34px;height:34px;border-radius:50%;background:var(--red)}
.foot-links{position:absolute;top:19px;font:400 9px/12.2px "PT Sans",sans-serif;color:#888}
.foot-links.a{left:296px}
.foot-links.b{left:341px;border-left:1px solid #444;padding-left:11px;height:50px}
.foot-head{position:absolute;top:18px;color:#fff;font:600 11.5px "Montserrat",sans-serif}
.socials{position:absolute;left:488px;top:50px;display:flex;gap:12px;font:700 10px "PT Sans",sans-serif;color:#777}
.socials span:first-child{color:#2a8fd0}
.signup{position:absolute;left:730px;top:46px;display:flex}
.signup div{width:133px;height:23px;background:#fff;color:#aaa;font-size:10px;padding:5px 9px}
.signup b{width:67px;height:23px;background:var(--red-deep);color:#fff;font:400 10px "PT Sans",sans-serif;display:flex;align-items:center;justify-content:center}
.copy{position:absolute;left:251px;top:80px;color:#666;font-size:9.5px}
</style>
</head>
<body>
<div class="side-photo left" role="img" aria-label="Player in red kit striking a ball in a floodlit stadium"></div>
<div class="side-photo right" role="img" aria-label="Player in blue kit making a high flying kick"></div>

<div class="topbar">
  <span class="auth">Login | Sign Up</span>
  <span class="network">NSL<br>NETWORK</span>
  <div class="crests">
    <i class="crest"></i><i class="crest"></i><i class="crest"></i><i class="crest"></i><i class="crest"></i><i class="crest"></i><i class="crest"></i><i class="crest"></i><i class="crest"></i><i class="crest"></i><i class="crest"></i><i class="crest"></i><i class="crest"></i><i class="crest"></i><i class="crest"></i><i class="crest"></i><i class="crest"></i><i class="crest"></i><i class="crest"></i>
    <span>NRT</span><span>ELM</span>
  </div>
  <div class="search">Search</div>
  <div class="feed"></div>
</div>

<header class="header">
  <div class="crest-logo">TREVMORA<br>FC</div>
  <nav class="nav">
    <a>HOME</a><a>NEWS</a><a>STATS</a><a>ABOUT</a><a>TICKETS</a><a>CONTACT</a><a>TEAM SHOP</a><a>THE RDL</a>
  </nav>
</header>

<main class="main">
  <section class="abs hero" role="img" aria-label="Player celebrating with arms raised in a red-toned stadium">
    <div class="hero-title">Trevmora<br>Football Club</div>
    <div class="hero-sub">KICKS OFF THIS SPRING!</div>
  </section>
  <div class="abs ticker">
    <div>HEADLINE/TITLE<small>Lorem ipsum dolor sit amet, consecte-</small></div>
    <div>HEADLINE/TITLE<small>Lorem ipsum dolor sit amet, consecte-</small></div>
    <div>HEADLINE/TITLE<small>Lorem ipsum dolor sit amet, consecte-</small></div>
  </div>

  <section class="abs standings">
    <div class="tab">STANDINGS</div>
    <table>
      <tr><th>POS</th><th>P</th><th>W</th><th>D</th><th>L</th></tr>
      <tr><td>1 - TEAM A</td><td>0</td><td>0</td><td>0</td><td>1</td></tr>
      <tr><td>2 - TEAM B</td><td>0</td><td>0</td><td>0</td><td>1</td></tr>
      <tr><td>3 - TEAM C</td><td>0</td><td>0</td><td>0</td><td>1</td></tr>
    </table>
  </section>
  <div class="abs video" role="img" aria-label="Video still of a player kicking a ball"><div class="video-bar"></div></div>

  <section class="abs card" style="left:15px">
    <div class="card-body">CATCH UP<br>WITH THE<br>STANDINGS<div class="card-art" role="img" aria-label="Young player juggling a ball"></div></div>
    <div class="tab">STATS</div>
  </section>
  <section class="abs card" style="left:255px">
    <div class="card-body">KNOW MORE<br>ABOUT OUR<br>TEAM<div class="card-art" role="img" aria-label="Two players heading a ball"></div></div>
    <div class="tab">ABOUT US</div>
  </section>
  <section class="abs card" style="left:495px">
    <div class="card-body">CHECK US<br>OUT ON<br>THE RADIO!<div class="radio-badge">WAVECAST<small>TREVMORA 101.7</small>Listen Now!</div></div>
    <div class="tab">WE'RE ON RADIO!</div>
  </section>

  <div class="abs tab news-tab">LATEST NEWS</div>
  <article class="abs news" style="top:496px">
    <div class="news-img" style="background:linear-gradient(135deg,#f3d23a,#e2362f)" role="img" aria-label="Club crest artwork close-up"></div>
    <h3>Official Press Release from the RDL on TRV...</h3>
    <p style="top:70px">Proin gravida nibh vel velit auctor aliquet. Aenean sollicitudin, lorem quis bibendum auctor, nisi elit consequat ipsum, nec sagittis sem nibh id elit.Proin gravida nibh vel velit auctor aliquet. Aenean sollicitudin, lorem</p>
  </article>
  <article class="abs news" style="top:616px">
    <div class="news-img" style="background:linear-gradient(160deg,#7a4a6a,#c03030)" role="img" aria-label="Supporter in club scarf at a radio interview"></div>
    <h3>Interview with the Morning Kettle!</h3>
    <p style="top:52px">Proin gravida nibh vel velit auctor aliquet. Aenean sollicitudin, loremProin gravida nibh vel velit auctor aliquet. Aenean sollicitudin, lorem quis bibendum auctor, nisi elit consequat ipsum, nec sagittis sem nibh id</p>
  </article>
  <article class="abs news" style="top:737px">
    <div class="news-img" style="background:linear-gradient(135deg,#555,#d89a2a 60%,#c02a2a)" role="img" aria-label="Goalkeeper diving for a save"></div>
    <h3>The Heart and Sol of Trevmora Sports</h3>
    <p style="top:64px">Proin gravida nibh vel velit auctor aliquet. Aenean sollicitudin, lorem quis bibendum auctor, nisi elit consequat ipsum, nec sagittis sem nibh id elit.Proin gravida nibh vel velit auctor aliquet. Aenean sollicitudin, lorem</p>
  </article>

  <section class="abs feed-box">
    <div class="feed-head"><i class="feed-dot"></i>Latest Chirper</div>
    <div class="feed-user"><i class="feed-avatar"></i><div><b>Trevmora</b><small>@Trevmora</small></div></div>
    <p class="feed-text">Lorem ipsum <em>#dolor</em> sit amet, consectet use adipiscing elit. Nunceri non massa utemi ante pelentesque ultricies.</p>
  </section>
  <div class="abs follow" style="left:497px;background:var(--sky)">FOLLOW US</div>
  <div class="abs follow" style="left:611px;background:var(--fb)">FOLLOW US</div>

  <aside class="abs ad" role="img" aria-label="Advertisement showing football boots on a purple smoky background">
    <div class="ad-text">Kelvaro<br>veltrazo 50</div>
    <div class="ad-cta">SHOP NOW</div>
  </aside>
</main>

<footer class="footer">
  <div class="foot-logo"></div>
  <div class="foot-links a">Home<br>News<br>Stats<br>About</div>
  <div class="foot-links b">Tickets<br>Contact<br>Team Shop<br>The RDL</div>
  <div class="foot-head" style="left:488px">SOCIAL MEDIA</div>
  <div class="socials"><span>Pagebook</span><span>Chirper</span><span>Circleplus</span><span>Linkwork</span><span>Feed</span></div>
  <div class="foot-head" style="left:730px">NEWSLETTER</div>
  <div class="signup"><div>Email Address</div><b>Subscribe</b></div>
  <div class="copy">Copyright 2014 Company Name | All Rights Reserved</div>
</footer>
</body>
</html>
```